Revamp Of Landing Page For an Automated AI Voice Agents Agency

here is my current landing page https://app.brightfunnelstudio.example/v2/preview/KXWQPmR4hLsDnTfYvJcA?notrack=true

Please use all my current content and imagery of ai agents in your new design. Make it easy to ready, easy to navigate and easy to understand

I am looking for a SLEEK shiny polished looking website. I like Dark themed sites but am open to see light themed sites too so please dont be shy.

The site should have an Ai Voice Agent Theme about it. Maybe look and feel of futureistic but simple and not intimidating to the average person...

Here are a couple website designs I like for reference:
https://q4t.example/
https://ai-bots.mervinholt.example/
https://chatvexo.example/ai-agents

Target Market(s)

b2b

Industry/Entity Type

AI Voice Agents

Coding

Coded - Design and coding required

Font styles to use
Other font styles liked:
• open

Requirements
Must have
• all elements and content and images used in existing design.
Nice to have
• open
Should not have
• open

```html
<!DOCTYPE html>
<html lang="en">
<head>
<meta charset="UTF-8">
<title>Voxara – Ai Voice Agents</title>
<link href="https://fonts.googleapis.com/css2?family=Montserrat:wght@400;500;600;700&display=swap" rel="stylesheet">
<style>
:root{
  --ink:#110d22;
  --hero-a:#1a0f4d;
  --hero-b:#5a12a8;
  --violet:#2a1266;
  --violet-b:#4a1f9a;
  --accent:#6b5fd1;
  --accent-2:#8a5ce0;
  --yellow:#ffe600;
  --blue:#1b5fb5;
  --white:#ffffff;
  --muted:#c9c4e6;
  --navy:#2a2380;
  --footer:#2b1470;
}
*{margin:0;padding:0;box-sizing:border-box}
html,body{width:1200px;height:4335px;overflow:hidden}
body{position:relative;background:var(--ink);font-family:'Montserrat',sans-serif;color:var(--white)}
.abs{position:absolute}
.center{left:0;width:1200px;text-align:center}
.band-hero{top:0;left:0;width:1200px;height:825px;background:radial-gradient(ellipse at 80% 30%,#3b2aa0 0%,transparent 55%),linear-gradient(160deg,var(--hero-a) 0%,#2a0f6e 50%,var(--hero-b) 100%)}
.band-violet{top:1957px;left:0;width:1200px;height:1234px;background:linear-gradient(160deg,var(--violet) 0%,#351790 55%,var(--violet-b) 100%)}
.band-footer{top:4268px;left:0;width:1200px;height:67px;background:var(--footer)}
.frame{top:20px;left:45px;width:1110px;height:4159px;border:2px solid rgba(255,255,255,.85)}
.logo{top:54px;font-size:42px;font-weight:500;letter-spacing:4px}
.hero-title{top:150px;left:120px;width:960px;text-align:center;font-size:31px;font-weight:500;line-height:1.35}
.btn{display:block;position:absolute;left:50%;transform:translateX(-50%);background:var(--yellow);color:#111;font-size:15px;font-weight:600;padding:8px 24px;border-radius:8px;text-decoration:none;white-space:nowrap}
.hero-box{top:417px;left:106px;width:490px;height:172px;background:var(--blue);border-radius:12px;border-bottom:8px solid var(--yellow);padding:20px 28px;font-size:15px;line-height:1.75;text-align:center;font-weight:500}
.img{background:linear-gradient(135deg,#2a3f8f,#5b2ac0)}
.h2{font-size:34px;font-weight:600;line-height:1.27}
.agent{width:298px;border:1px solid rgba(255,255,255,.7);background:var(--ink)}
.agent .img{height:337px}
.agent h3{font-size:19px;font-weight:500;color:var(--accent-2);margin:18px 17px 12px}
.agent p{font-size:12.5px;line-height:1.75;margin:0 17px 16px}
.nav{width:42px;height:42px;border:2px solid #fff;border-radius:50%}
.note{left:100px;width:1000px;text-align:center;font-size:15px;line-height:1.8}
.h-white{font-size:32px;font-weight:500}
.feature{width:298px;height:225px;border:1px solid rgba(255,255,255,.6);border-radius:10px;text-align:center}
.feature svg{margin-top:14px}
.feature h4{font-size:19px;font-weight:600;margin-top:14px}
.feature p{font-size:13px;line-height:1.7;margin-top:10px;color:var(--muted)}
.promise{left:111px;width:446px;height:103px;border:1px solid rgba(255,255,255,.7);border-radius:12px;display:flex;align-items:center;gap:28px;padding-left:80px;font-size:19px;font-weight:500;line-height:1.4}
.faq-q{left:646px;width:443px;font-size:14px;padding:0 18px;display:flex;justify-content:space-between;align-items:center;border:1px solid rgba(255,255,255,.6)}
.faq-q span.t{font-weight:500}
.tog{width:20px;height:20px;background:var(--navy);color:#fff;font-size:14px;line-height:18px;text-align:center}
</style>
</head>
<body>
<div class="abs band-hero"></div>
<div class="abs band-violet"></div>
<div class="abs band-footer"></div>
<div class="abs frame"></div>

<!-- Hero -->
<div class="abs center logo">VOXARA</div>
<h1 class="abs hero-title">Ai Voice Agents That Answer Calls, Book Appts, Send Emails, Text Messages, Follow Up Reminders, Transfer Calls &amp; More For You 24 Hours 7 Days A Week!</h1>
<a class="btn" style="top:300px" href="#">Get An Instant Free Demo</a>
<div class="abs hero-box">We Will Create An Ai Agent Customized For Your Business At No Cost. Simply Click The Button Above And Your Very Own Ai Agent Will Be Calling You In Just A Couple Minutes. Experience The Magic And Get Ready To Be Very Impressed!</div>
<svg class="abs" style="top:450px;left:620px" width="135" height="55" viewBox="0 0 135 55"><path d="M4 14 C45 2 95 8 122 38" stroke="#fff" stroke-width="9" fill="none" stroke-linecap="round"/><path d="M102 36 L128 46 L124 18 Z" fill="#fff"/></svg>
<div class="abs img" role="img" aria-label="Friendly robot with headset typing on a pink laptop" style="top:370px;left:640px;width:462px;height:413px;border-radius:40px;background:radial-gradient(circle at 60% 35%,#8a8fff 0%,#5a3ad0 40%,transparent 72%),radial-gradient(circle at 35% 80%,#ff4fd8 0%,transparent 45%)"></div>

<!-- Workforce -->
<h2 class="abs center h2" style="top:903px;color:var(--accent)">Meet Your New<br>AI- Powered Workforce</h2>
<div class="abs agent" style="top:1069px;left:111px">
  <div class="img" role="img" aria-label="Ai receptionist in headset" style="background:linear-gradient(150deg,#2fb8d6,#1c4e6e 60%,#0c2035)"></div>
  <h3>Ai Receptionist</h3>
  <p>Cody handles all your calls 24/7. You can also set him to only take overflow calls and after hours.</p>
</div>
<div class="abs agent" style="top:1040px;left:451px">
  <div class="img" role="img" aria-label="Ai sales agent at desk with city view" style="background:linear-gradient(150deg,#dfe5ea,#7f8a95 55%,#2a3036)"></div>
  <h3>Ai Sales Agent</h3>
  <p>Brian will take your inbound sales calls. Will give all detailed information to the customer, answer questions</p>
</div>
<div class="abs agent" style="top:1069px;left:791px">
  <div class="img" role="img" aria-label="Ai appointment setter typing with headset" style="background:linear-gradient(150deg,#3aa6c4,#1d5c78 55%,#0e2a3a)"></div>
  <h3>Ai Appointment Setter</h3>
  <p>Bobby offers business advice, helps brainstorm ideas, and provides insights on growth tactics to support</p>
</div>
<div class="abs nav" style="top:1588px;left:544px"><svg width="38" height="38" viewBox="0 0 38 38"><path d="M21 13 L15 19 L21 25" stroke="#fff" stroke-width="2" fill="none"/></svg></div>
<div class="abs nav" style="top:1588px;left:612px"><svg width="38" height="38" viewBox="0 0 38 38"><path d="M17 13 L23 19 L17 25" stroke="#fff" stroke-width="2" fill="none"/></svg></div>
<p class="abs note" style="top:1696px">We Will Create An Ai Agent Customized For Your Business At No Cost. Simply Click The Button Above And Your Very Own Ai Agent Will Be Calling You In Just A Couple Minutes. Experience The Magic And Get Ready To Be Very Impressed!</p>
<h2 class="abs center h-white" style="top:1775px">Install The Power Of Ai For Your Business</h2>
<a class="btn" style="top:1841px" href="#">Get An Instant Free Demo</a>

<!-- Wish -->
<div class="abs img" role="img" aria-label="White robot with headset holding a laptop" style="top:2045px;left:111px;width:285px;height:353px;border-radius:30px;background:radial-gradient(circle at 45% 40%,#e6e8f0 0%,#9aa0b8 35%,transparent 70%)"></div>
<h2 class="abs h2" style="top:2084px;left:508px;color:var(--accent-2)">Your Wish Is<br>Their Command</h2>
<p class="abs" style="top:2200px;left:508px;width:590px;font-size:22px;font-weight:500;line-height:1.4">Your New Ai Agents Will Never Call In Sick And Will Never Complain!</p>
<p class="abs" style="top:2277px;left:508px;width:590px;font-size:14.5px;line-height:1.75;color:var(--muted)">With your new team of AI Agents, handling inbound calls, sending emails and sms messages, booking appointments and handling customer service inquiries is going to save you a ton of time and money.</p>
<div class="abs" style="top:2486px;left:111px;width:978px;height:1px;background:rgba(255,255,255,.35)"></div>
<h2 class="abs center h2" style="top:2566px;color:var(--accent-2)">An Employee That Never Gets Sick!</h2>
<div class="abs feature" style="top:2656px;left:111px">
  <svg width="90" height="90" viewBox="0 0 90 90" fill="none" stroke="#fff" stroke-width="2"><path d="M45 12 C30 12 18 22 18 38 C12 42 12 56 20 60 C22 72 34 78 45 76 C56 78 68 72 70 60 C78 56 78 42 72 38 C72 22 60 12 45 12 Z"/><path d="M45 12 V76 M30 30 H45 M45 46 H62 M28 56 H45 M58 24 V34"/><circle cx="30" cy="30" r="3"/><circle cx="62" cy="46" r="3"/><circle cx="28" cy="56" r="3"/></svg>
  <h4>Trained In Seconds</h4>
  <p>Learns Your Entire Website<br>In Seconds</p>
</div>
<div class="abs feature" style="top:2656px;left:451px">
  <svg width="90" height="90" viewBox="0 0 90 90" fill="none" stroke="#fff" stroke-width="2"><circle cx="45" cy="45" r="30"/><circle cx="45" cy="45" r="36" stroke-dasharray="4 4"/><ellipse cx="45" cy="45" rx="13" ry="30"/><path d="M15 45 H75 M19 31 H71 M19 59 H71 M45 15 V75"/></svg>
  <h4>Worldwide</h4>
  <p>Works Anywhere In The<br>Globe</p>
</div>
<div class="abs feature" style="top:2656px;left:791px">
  <svg width="90" height="90" viewBox="0 0 90 90" fill="none" stroke="#fff" stroke-width="3" stroke-linecap="round"><circle cx="40" cy="30" r="15"/><path d="M14 76 C14 58 26 48 40 48 C46 48 51 50 55 53"/><path d="M52 68 L60 76 L76 58"/></svg>
  <h4>User-Friendly</h4>
  <p>Your Ai Agents Sound As If<br>They're Real Humans</p>
</div>
<p class="abs note" style="top:2932px">We Will Create An Ai Agent Customized For Your Business At No Cost. Simply Click The Button Above And Your Very Own Ai Agent Will Be Calling You In Just A Couple Minutes. Experience The Magic And Get Ready To Be Very Impressed!</p>
<h2 class="abs center h-white" style="top:3010px">Our Ai Agents Our Ready To Be Hired</h2>
<a class="btn" style="top:3073px" href="#">Get An Instant Free Demo</a>

<!-- Reviews & FAQ -->
<h2 class="abs center" style="top:3268px;font-size:30px;font-weight:500;line-height:1.4">After Our Customers Have A Conversation With Their New<br>Ai Voice Agent They Give Us 5 Stars!</h2>
<svg class="abs" style="top:3382px;left:532px" width="136" height="26" viewBox="0 0 136 26"><g fill="#f5b400"><path id="s" d="M13 1 L16.5 9 L25 9.6 L18.5 15 L20.5 23.5 L13 19 L5.5 23.5 L7.5 15 L1 9.6 L9.5 9 Z"/><use href="#s" x="27"/><use href="#s" x="54"/><use href="#s" x="81"/><use href="#s" x="108"/></g></svg>
<h2 class="abs h2" style="top:3491px;left:111px;color:var(--accent)">Our Promise To You</h2>
<h2 class="abs h2" style="top:3491px;left:646px;color:var(--accent)">Do You Have Questions?</h2>
<div class="abs promise" style="top:3573px;padding-left:80px">
  <svg width="62" height="62" viewBox="0 0 62 62"><path d="M31 3 L37 8 L45 6 L48 14 L56 17 L54 25 L59 31 L54 37 L56 45 L48 48 L45 56 L37 54 L31 59 L25 54 L17 56 L14 48 L6 45 L8 37 L3 31 L8 25 L6 17 L14 14 L17 6 L25 8 Z" fill="#fff"/><circle cx="31" cy="31" r="17" fill="none" stroke="#111" stroke-width="2.5"/><path d="M23 31 L29 37 L40 25" stroke="#111" stroke-width="3" fill="none"/></svg>
  <span>14-day Money-back<br>Guarantee*</span>
</div>
<div class="abs promise" style="top:3706px">
  <svg width="62" height="62" viewBox="0 0 62 62" fill="#fff"><circle cx="31" cy="20" r="11"/><path d="M16 20 A15 15 0 0 1 46 20" fill="none" stroke="#fff" stroke-width="3"/><rect x="12" y="17" width="6" height="10" rx="2"/><rect x="44" y="17" width="6" height="10" rx="2"/><path d="M14 52 C14 40 22 34 31 34 C40 34 48 40 48 52 Z"/><rect x="20" y="42" width="22" height="14" fill="#111" stroke="#fff" stroke-width="2"/><rect x="10" y="56" width="42" height="4"/></svg>
  <span>24/7 Customer<br>Support</span>
</div>
<div class="abs" style="top:3587px;left:601px;width:1px;height:203px;background:rgba(255,255,255,.5)"></div>
<div class="abs faq-q" style="top:3575px;height:33px;background:var(--navy);border-color:var(--navy)"><span class="t">What exactly are the AI Voice Agents?</span><span>–</span></div>
<div class="abs" style="top:3608px;left:646px;width:443px;height:85px;background:#fff;color:#666;font-size:11.5px;line-height:1.75;padding:10px 18px">AI Voice Agents are specialized human sounding bots, having smart and masterful conversations and each is expertly trained in seconds for a specific business function.</div>
<div class="abs faq-q" style="top:3713px;height:34px"><span class="t">How will these AI Voice Agents benefit</span><span class="tog">–</span></div>
<div class="abs faq-q" style="top:3763px;height:34px"><span class="t">Are they easy to use?</span><span class="tog">–</span></div>
<p class="abs note" style="top:3866px">We Will Create An Ai Agent Customized For Your Business At No Cost. Simply Click The Button Above And Your Very Own Ai Agent Will Be Calling You In Just A Couple Minutes. Experience The Magic And Get Ready To Be Very Impressed!</p>
<h2 class="abs center h-white" style="top:3948px;line-height:1.3">These AI Agents Can Help<br>Your Business Tremendously. Imagine The Possibilities</h2>
<a class="btn" style="top:4062px" href="#">Get An Instant Free Demo</a>

<!-- Footer -->
<div class="abs" style="top:4292px;left:111px;font-size:12.5px">© 2025 Voxara</div>
<div class="abs" style="top:4292px;left:695px;width:394px;text-align:right;font-size:12.5px">Privacy | Terms &amp; Conditions | Earnings &amp; Products Disclaimer</div>
</body>
</html>
```